Hvac service truck vinyl decals

2023 q480 RTV
You can find the logo i want to use at
kelmovent.com
Include
Logo
Don't Sweat, Call Kelmo!
Website
Ph# 9851937046

```html
<!DOCTYPE html>
<html lang="en">
<head>
<meta charset="utf-8">
<title>Kelmo Vent – Truck Side Decal</title>
<link href="https://fonts.googleapis.com/css2?family=Bebas+Neue&display=swap" rel="stylesheet">
<style>
  :root {
    --canvas: #ffffff;
    --panel-top: #e6e6e6;
    --panel-mid: #fbfbfb;
    --panel-bottom: #e9e9e9;
    --stripe-white: #ffffff;
    --sky-blue: #42a3dc;
    --signal-red: #f2070f;
    --ink: #0b0b0b;
  }
  html, body {
    margin: 0;
    padding: 0;
    width: 1200px;
    height: 1070px;
    overflow: hidden;
    background: var(--canvas);
  }
  .canvas {
    position: relative;
    width: 1200px;
    height: 1070px;
  }
  .decal {
    position: absolute;
    left: 50px;
    top: 358px;
    width: 1100px;
    height: 354px;
    background: linear-gradient(180deg, var(--panel-top) 0%, var(--panel-mid) 30%, var(--panel-mid) 72%, var(--panel-bottom) 100%);
    overflow: hidden;
    font-family: "Bebas Neue", "Arial Narrow", sans-serif;
  }
  .decal__stripes {
    position: absolute;
    inset: 0;
  }
  .tagline {
    position: absolute;
    left: 76px;
    top: 62px;
    display: flex;
    align-items: flex-end;
    gap: 8px;
    line-height: 0.8;
  }
  .tagline__lead {
    color: var(--sky-blue);
    font-size: 48px;
    text-align: right;
    letter-spacing: -1px;
    paint-order: stroke fill;
    -webkit-text-stroke: 4px var(--stripe-white);
  }
  .tagline__call,
  .tagline__name {
    font-size: 112px;
    letter-spacing: -2px;
    paint-order: stroke fill;
    -webkit-text-stroke: 6px var(--stripe-white);
  }
  .tagline__call { color: var(--signal-red); margin-right: 10px; }
  .tagline__name { color: var(--sky-blue); }
  .phone {
    position: absolute;
    left: 76px;
    top: 166px;
    color: var(--ink);
    font-size: 104px;
    line-height: 1;
    letter-spacing: -2px;
    word-spacing: 4px;
    paint-order: stroke fill;
    -webkit-text-stroke: 6px var(--stripe-white);
  }
  .brand {
    position: absolute;
    left: 615px;
    top: 120px;
    display: flex;
    align-items: center;
    gap: 14px;
  }
  .brand__dot {
    width: 54px;
    height: 54px;
    border-radius: 50%;
    background: var(--signal-red);
  }
  .brand__name {
    color: var(--sky-blue);
    font-size: 72px;
    line-height: 1;
    letter-spacing: 1px;
  }
  .website {
    position: absolute;
    right: 48px;
    top: 216px;
    color: var(--stripe-white);
    font-size: 34px;
    letter-spacing: 2px;
    line-height: 1;
  }
</style>
</head>
<body>
<main class="canvas">
  <section class="decal" aria-label="Kelmo Vent truck side decal">
    <svg class="decal__stripes" width="1100" height="354" viewBox="0 0 1100 354" aria-hidden="true">
      <path d="M0 186 C 40 178, 60 160, 120 160 L 1100 160 L 1100 206 L 0 206 Z" fill="var(--stripe-white)"/>
      <path d="M0 204 L 1100 204 L 1096 262 L 8 262 Z" fill="var(--sky-blue)"/>
      <path d="M8 262 L 1096 262 L 1093 271 L 10 271 Z" fill="var(--signal-red)"/>
    </svg>

    <div class="tagline">
      <div class="tagline__lead">Don't<br>Sweat</div>
      <div class="tagline__call">Call</div>
      <div class="tagline__name">Kelmo!</div>
    </div>

    <div class="phone">985 1 937 046</div>

    <div class="brand">
      <span class="brand__dot" aria-hidden="true"></span>
      <span class="brand__name">Kelmo Vent</span>
    </div>

    <div class="website">kelmovent.com</div>
  </section>
</main>
</body>
</html>
```